Health software company called BRIGHT MERIDIAN, committed to innovation and technological excellence

The powerpoint presentation template is necessary, very necessary is elegant and modern with innovative images and the color palette attached. The presentation will be used for the business plan and investor presentations that we will use to raise funds. Please, recommend a modern typeface, as well as format to be able to use it and incorporate it as part of the company's brand guidelines. Great diversity of technological solutions
Updates

Very low attendance of designers for a high budget. Very few proposals and no capture my interest

Need extra days to review

Need extra days to review

Need extra days to review

Target Market(s)

managers, managers of public and private health centers, government states, investors

Industry/Entity Type

It Company

Font styles to use
Serif

Requirements
Must have
• The powerpoint presentation template is necessary, very necessary is elegant, minimalist and modern with innovative images and the color palette attached. it must be refined in demarcated style
Nice to have
• very nice, visually harmonic avoid saturation
Should not have
• NO dark colors NO dark colors NO dark colors NO dark colors NO dark colors

```html
<!DOCTYPE html>
<html lang="en">
<head>
<meta charset="utf-8">
<title>Bright Meridian – Presentation Template</title>
<link rel="stylesheet" href="https://fonts.googleapis.com/css2?family=Oswald:wght@500&family=Montserrat:wght@400;500&family=Open+Sans:wght@400;600;700&display=swap">
<style>
  :root{
    --ink:#1c1c1c;
    --muted:#555;
    --rule:#9a9a9a;
    --paper:#ffffff;
    --sky:#00b4ef;
    --grey-band:#b3b3b3;
    --step-grey:#a7a7a7;
    --step-blue:#6fcdf2;
    --step-green:#b9dc8f;
    --step-orange:#fbbd7c;
    --step-purple:#b782c0;
    --step-pink:#f291c3;
    --hub-outer:#ececec;
    --hub-inner:#e4e4e6;
  }
  html,body{margin:0;padding:0;overflow:hidden;}
  body{width:1200px;height:761px;background:var(--paper);position:relative;font-family:"Open Sans",sans-serif;color:var(--ink);}
  .slide{position:absolute;width:568px;height:320px;box-shadow:0 0 4px rgba(0,0,0,.35);background:var(--paper);}
  .slide svg{display:block;width:568px;height:320px;}
  .slide--cover{left:20px;top:22px;}
  .slide--back{left:612px;top:22px;}
  .slide--about{left:20px;top:392px;}
  .slide--steps{left:612px;top:392px;}
  .slide-label{position:absolute;width:568px;text-align:center;font-family:"Open Sans",sans-serif;font-size:16px;color:#333;letter-spacing:.3px;}
  .display{font-family:"Oswald",sans-serif;font-weight:500;fill:var(--ink);}
  .caps{font-family:"Montserrat",sans-serif;font-weight:500;fill:var(--ink);letter-spacing:.6px;}
  .body{font-family:"Open Sans",sans-serif;fill:var(--ink);}
  .accent{font-family:"Open Sans",sans-serif;font-weight:700;fill:var(--sky);}
  .bold{font-weight:700;}
</style>
</head>
<body>

<!-- Cover page -->
<div class="slide slide--cover">
<svg viewBox="0 0 710 400" xmlns="http://www.w3.org/2000/svg">
  <defs>
    <linearGradient id="officeTones" x1="0" y1="0" x2="1" y2="1">
      <stop offset="0" stop-color="#4f6b3e"/>
      <stop offset=".5" stop-color="#c9b4ad"/>
      <stop offset="1" stop-color="#e9e9e9"/>
    </linearGradient>
  </defs>
  <polygon points="235,0 257,0 412,222 390,222" fill="var(--grey-band)"/>
  <polygon points="257,0 710,0 710,400 512,400" fill="url(#officeTones)" role="img" aria-label="Photo of a smiling businesswoman on the phone working at a laptop"/>
  <polygon points="268,400 390,212 512,400" fill="var(--sky)"/>
  <rect x="21.5" y="21.5" width="162" height="42" fill="none" stroke="var(--ink)" stroke-width="1.2"/>
  <text class="display" x="102.5" y="51" font-size="22" text-anchor="middle">BRIGHT MERIDIAN</text>
  <text class="display" x="21" y="206" font-size="25">LOREM IPSUM IS SIMPLY DUMMY</text>
  <text class="body" x="22" y="226" font-size="13">Lorem Ipsum is simply dummy text of the printing</text>
  <text class="body" x="22" y="242" font-size="13">and typesetting industry.</text>
  <text class="body" x="21" y="377" font-size="8.5">www.brightmeridian-health.com</text>
  <line x1="142" y1="374.5" x2="290" y2="374.5" stroke="var(--rule)" stroke-width=".8"/>
</svg>
</div>
<div class="slide-label" style="left:20px;top:356px;">COVER PAGE</div>

<!-- Back page -->
<div class="slide slide--back">
<svg viewBox="0 0 710 400" xmlns="http://www.w3.org/2000/svg">
  <defs>
    <linearGradient id="corridorTones" x1="0" y1="0" x2="1" y2="0">
      <stop offset="0" stop-color="#eef0f2"/>
      <stop offset=".6" stop-color="#dcd6d2"/>
      <stop offset="1" stop-color="#e8e9eb"/>
    </linearGradient>
  </defs>
  <polygon points="355,0 710,0 710,400" fill="url(#corridorTones)" role="img" aria-label="Faded photo of a businesswoman walking while on the phone"/>
  <polygon points="452,400 580,252 710,400" fill="var(--sky)"/>
  <text class="display" x="21" y="41" font-size="22">LOREM IPSUM IS SIMPLY DUMMY TEXT</text>
  <rect x="21.5" y="93.5" width="162" height="42" fill="none" stroke="var(--ink)" stroke-width="1.2"/>
  <text class="display" x="102.5" y="123" font-size="22" text-anchor="middle">BRIGHT MERIDIAN</text>
  <text class="caps" x="21" y="200" font-size="15.5">CONTACT INFORMATION</text>
  <line x1="21" y1="206" x2="208" y2="206" stroke="var(--ink)" stroke-width=".8"/>
  <g class="body" font-size="8.5">
    <circle cx="25" cy="229" r="3" fill="var(--ink)"/>
    <text x="33" y="232">Lorem Ipsum 143, 2nd Floor, Lorem Ipsum,</text>
    <text x="33" y="244">Lorem Ipsum is simply dummy</text>
    <circle cx="25" cy="258" r="3" fill="var(--ink)"/>
    <text x="33" y="261">123456</text>
    <circle cx="25" cy="275" r="3" fill="var(--ink)"/>
    <text x="33" y="278">+987 6 50210</text>
    <circle cx="25" cy="292" r="3" fill="var(--ink)"/>
    <text x="33" y="295">hello@brightmeridian-health.com</text>
  </g>
  <text class="body" x="21" y="377" font-size="8.5">www.brightmeridian-health.com</text>
  <line x1="142" y1="374.5" x2="470" y2="374.5" stroke="var(--rule)" stroke-width=".8"/>
</svg>
</div>
<div class="slide-label" style="left:612px;top:356px;">BACK PAGE</div>

<!-- Page 01 : About us -->
<div class="slide slide--about">
<svg viewBox="0 0 710 400" xmlns="http://www.w3.org/2000/svg">
  <rect x="20.5" y="16.5" width="50" height="12" fill="none" stroke="var(--ink)" stroke-width=".6"/>
  <text class="display" x="45.5" y="25.5" font-size="6" text-anchor="middle">BRIGHT MERIDIAN</text>
  <line x1="72" y1="22" x2="710" y2="22" stroke="var(--ink)" stroke-width="1.2"/>
  <text class="caps" x="20" y="59" font-size="14.5">ABOUT US</text>
  <g class="body" font-size="7.2">
    <text x="20" y="75">Lorem Ipsum is simply dummy text of the printing and typesetting industry. Lorem Ipsum has been the industry's standard dummy text ever since the 1500s, when an unknown printer took</text>
    <text x="20" y="88">a galley of type and scrambled it to make a type specimen book. It has survived not only five centuries, but also the leap into electronic typesetting, remaining essentially unchanged. Lorem</text>
    <text x="20" y="101">Ipsum is simply dummy text of the printing and typesetting industry. Lorem Ipsum has been the industry's standard dummy text ever since the 1500s.</text>
  </g>

  <g class="timeline">
    <rect x="62" y="222" width="116" height="12" fill="var(--step-grey)"/>
    <rect x="178" y="222" width="118" height="12" fill="var(--step-blue)"/>
    <rect x="296" y="222" width="117" height="12" fill="var(--step-green)"/>
    <rect x="413" y="222" width="117" height="12" fill="var(--step-orange)"/>
    <rect x="530" y="222" width="116" height="12" fill="var(--step-purple)"/>
    <circle cx="62" cy="228" r="14" fill="var(--step-grey)" stroke="#fff" stroke-width="2"/>
    <circle cx="178" cy="228" r="14" fill="var(--step-blue)" stroke="#fff" stroke-width="2"/>
    <circle cx="296" cy="228" r="14" fill="var(--step-green)" stroke="#fff" stroke-width="2"/>
    <circle cx="413" cy="228" r="14" fill="var(--step-orange)" stroke="#fff" stroke-width="2"/>
    <circle cx="530" cy="228" r="14" fill="var(--step-purple)" stroke="#fff" stroke-width="2"/>
    <circle cx="646" cy="228" r="14" fill="var(--step-pink)" stroke="#fff" stroke-width="2"/>
    <g fill="none" stroke="#fff" stroke-width="1.3">
      <circle cx="62" cy="228" r="5"/>
      <rect x="171" y="222" width="14" height="10"/>
      <circle cx="296" cy="228" r="6"/>
      <rect x="406" y="223" width="14" height="10"/>
      <ellipse cx="530" cy="228" rx="8" ry="3.5"/>
      <ellipse cx="530" cy="228" rx="3.5" ry="8"/>
      <circle cx="646" cy="228" r="6"/>
      <line x1="640" y1="228" x2="652" y2="228"/>
    </g>
    <polygon points="57,248 67,248 62,255" fill="var(--step-grey)"/>
    <polygon points="173,205 183,205 178,198" fill="var(--step-blue)"/>
    <polygon points="291,248 301,248 296,255" fill="var(--step-green)"/>
    <polygon points="408,205 418,205 413,198" fill="var(--step-orange)"/>
    <polygon points="525,248 535,248 530,255" fill="var(--step-purple)"/>
    <polygon points="641,205 651,205 646,198" fill="var(--step-pink)"/>

    <g class="body" font-size="5" text-anchor="middle">
      <text class="bold" x="62" y="265">STEP 01</text>
      <text class="bold" x="178" y="196">STEP 02</text>
      <text class="bold" x="296" y="265">STEP 03</text>
      <text class="bold" x="413" y="196">STEP 04</text>
      <text class="bold" x="530" y="265">STEP 05</text>
      <text class="bold" x="646" y="196">STEP 06</text>

      <text class="bold" x="62" y="180" font-size="6">TITLE</text>
      <text x="62" y="189">Lorem Ipsum is simply dummy</text>
      <text x="62" y="196">text of the printing and typesetting</text>
      <text x="62" y="203">industry.</text>

      <text class="bold" x="296" y="180" font-size="6">TITLE</text>
      <text x="296" y="189">Lorem Ipsum is simply dummy</text>
      <text x="296" y="196">text of the printing and typesetting</text>
      <text x="296" y="203">industry.</text>

      <text class="bold" x="530" y="180" font-size="6">TITLE</text>
      <text x="530" y="189">Lorem Ipsum is simply dummy</text>
      <text x="530" y="196">text of the printing and typesetting</text>
      <text x="530" y="203">industry.</text>

      <text class="bold" x="178" y="256" font-size="6">TITLE</text>
      <text x="178" y="265">Lorem Ipsum is simply dummy</text>
      <text x="178" y="272">text of the printing and typesetting</text>
      <text x="178" y="279">industry.</text>

      <text class="bold" x="413" y="256" font-size="6">TITLE</text>
      <text x="413" y="265">Lorem Ipsum is simply dummy</text>
      <text x="413" y="272">text of the printing and typesetting</text>
      <text x="413" y="279">industry.</text>

      <text class="bold" x="646" y="256" font-size="6">TITLE</text>
      <text x="646" y="265">Lorem Ipsum is simply dummy</text>
      <text x="646" y="272">text of the printing and typesetting</text>
      <text x="646" y="279">industry.</text>
    </g>
  </g>

  <polygon points="620,400 710,310 710,400" fill="var(--sky)"/>
  <text class="body" x="20" y="377" font-size="6">www.brightmeridian-health.com</text>
  <line x1="112" y1="375" x2="660" y2="375" stroke="var(--rule)" stroke-width=".6"/>
  <text class="body" x="681" y="378" font-size="5.5">01</text>
</svg>
</div>
<div class="slide-label" style="left:20px;top:731px;">PAGE 01</div>

<!-- Page 02 : Six steps -->
<div class="slide slide--steps">
<svg viewBox="0 0 710 400" xmlns="http://www.w3.org/2000/svg">
  <defs>
    <linearGradient id="hubRing" x1="0" y1="0" x2="0" y2="1">
      <stop offset="0" stop-color="var(--hub-outer)"/>
      <stop offset="1" stop-color="#fafafa"/>
    </linearGradient>
  </defs>
  <rect x="20.5" y="16.5" width="50" height="12" fill="none" stroke="var(--ink)" stroke-width=".6"/>
  <text class="display" x="45.5" y="25.5" font-size="6" text-anchor="middle">BRIGHT MERIDIAN</text>
  <line x1="72" y1="22" x2="710" y2="22" stroke="var(--ink)" stroke-width="1.2"/>
  <text class="caps" x="20" y="58" font-size="14">LOREM IPSUM IS SIMPLY DUMMY TEXT OF THE PRINTING AND TYPESETTING INDUSTRY</text>

  <circle cx="344" cy="208" r="92" fill="url(#hubRing)"/>
  <circle cx="344" cy="208" r="72" fill="var(--hub-inner)" stroke="#fff" stroke-width="3"/>
  <rect x="284.5" y="194.5" width="120" height="27" fill="#fff" stroke="var(--ink)" stroke-width="1"/>
  <text class="display" x="344.5" y="213.5" font-size="13.5" text-anchor="middle">BRIGHT MERIDIAN</text>

  <g fill="none" stroke="var(--ink)" stroke-width=".8">
    <polyline points="212,108 262,108 262,134 305,134"/>
    <polyline points="212,198 280,198"/>
    <polyline points="212,302 262,302 262,276 305,276"/>
    <polyline points="480,108 430,108 430,134 390,134"/>
    <polyline points="480,198 424,198"/>
    <polyline points="480,302 430,302 430,276 390,276"/>
  </g>
  <g fill="var(--ink)">
    <circle cx="212" cy="108" r="1.5"/><circle cx="212" cy="198" r="1.5"/><circle cx="212" cy="302" r="1.5"/>
    <circle cx="480" cy="108" r="1.5"/><circle cx="480" cy="198" r="1.5"/><circle cx="480" cy="302" r="1.5"/>
  </g>

  <g font-size="8">
    <text class="accent" x="207" y="111" text-anchor="end">STEP 01</text>
    <text class="accent" x="207" y="201" text-anchor="end">STEP 02</text>
    <text class="accent" x="207" y="305" text-anchor="end">STEP 03</text>
    <text class="accent" x="485" y="111">STEP 04</text>
    <text class="accent" x="485" y="201">STEP 05</text>
    <text class="accent" x="485" y="305">STEP 06</text>
  </g>
  <g class="body" font-size="7.4">
    <g text-anchor="end">
      <text x="206" y="127">Lorem Ipsum is simply dummy text of</text>
      <text x="206" y="140">the printing and typesetting.</text>
      <text x="206" y="216">Lorem Ipsum is simply dummy text of</text>
      <text x="206" y="229">the printing and typesetting industry.</text>
      <text x="206" y="320">Lorem Ipsum is simply dummy text of</text>
      <text x="206" y="333">the printing and typesetting.</text>
    </g>
    <text x="486" y="128">Lorem Ipsum is simply dummy text of the</text>
    <text x="486" y="141">printing and typesetting industry.</text>
    <text x="486" y="216">Lorem Ipsum is simply dummy text of the</text>
    <text x="486" y="229">printing and typesetting industry.</text>
    <text x="486" y="318">Lorem Ipsum is simply dummy text of the</text>
    <text x="486" y="331">printing and typesetting industry.</text>
  </g>

  <polygon points="620,400 710,310 710,400" fill="var(--sky)"/>
  <text class="body" x="20" y="377" font-size="6">www.brightmeridian-health.com</text>
  <line x1="112" y1="375" x2="660" y2="375" stroke="var(--rule)" stroke-width=".6"/>
  <text class="body" x="681" y="378" font-size="5.5">02</text>
</svg>
</div>
<div class="slide-label" style="left:612px;top:731px;">PAGE 02</div>

</body>
</html>
```